Business card design needed

Need a simple slim business card. Wanted it in a royal or deep blue with platinum or silver writing.
Front to be to say LARKMOOR CORPORATE CARS with website address www.lkcx.com.au underneath in smaller text. Need a relevant logo to match title something elegant and classy.
At the back I would like name and then underneath mobile and email. Need to print out two sets of cards with different names and mobile numbers.
Under contact details in bullet form
*airport transfers *corporate travel *special occasions *tours
Then under that the logo and symbols of Continental Tender card PayCrest, Zelo card, supper guild and rideslip.
Want all text embossed and texture of card a velvet material.
Email on back should be bookings@lkcx.com.au

Email on back of card should be bookings@lkcx.com.au my mistake sorry

A really dark navy blue
Elegant shiny silver writing
Must say Larkmoor Corporate Cars on front with a logo/symbol that describes the business or business name or both?
The names on back will be seperate. So half of the cards printed will have Dean Kovalik and mobile number. Next half of cards printed will have Martin Kovalik and mobile. So not the 2 names on back of card.

Travel

Half card with name Dean Kovalik mob 0400193726
Other half cards Martin Kovalik 0400862051
Email in both bookings@larkmoorlimos.com

```html
<!DOCTYPE html>
<html lang="en">
<head>
<meta charset="utf-8">
<title>Larkmoor Corporate Cars – Business Card</title>
<link rel="stylesheet" href="https://fonts.googleapis.com/css2?family=PT+Sans:wght@400;700&display=swap">
<style>
  :root {
    --page-bg: #e9e9ec;
    --navy-core: #2a347a;
    --navy-mid: #1b245c;
    --navy-edge: #0f163d;
    --silver-light: #f2f3f5;
    --silver-mid: #c4c7ce;
    --silver-dark: #8d9099;
    --ink-dark: #15182a;
    --text-soft: #c9cde0;
    --chip: #4a5288;
    --white: #ffffff;
  }
  * { margin: 0; padding: 0; box-sizing: border-box; }
  html, body {
    width: 1200px; height: 1000px; overflow: hidden;
    background: var(--page-bg);
    font-family: "PT Sans", "Segoe UI", sans-serif;
  }
  .card-set {
    position: absolute; top: 349px; left: 46px;
    display: flex; gap: 34px;
  }
  .card {
    position: relative; width: 537px; height: 302px;
    border-radius: 12px;
    background: radial-gradient(ellipse 70% 75% at 50% 45%, var(--navy-core) 0%, var(--navy-mid) 55%, var(--navy-edge) 100%);
    box-shadow: 0 6px 14px rgba(0,0,0,.35);
    overflow: hidden;
  }
  .silver-text {
    background: linear-gradient(180deg, var(--silver-light) 0%, var(--silver-mid) 55%, var(--silver-dark) 100%);
    -webkit-background-clip: text; background-clip: text;
    color: transparent;
  }
  /* front */
  .brand-mark {
    position: absolute; top: 62px; left: 0; width: 100%;
    text-align: center;
    font-size: 30px; font-weight: 400; letter-spacing: 4px;
    color: var(--silver-mid);
  }
  .company-name {
    position: absolute; top: 155px; width: 100%; text-align: center;
    font-size: 22px; font-weight: 400; letter-spacing: .3px;
  }
  .company-web {
    position: absolute; top: 183px; width: 100%; text-align: center;
    font-size: 16px; color: var(--silver-mid);
  }
  /* back */
  .person-name {
    position: absolute; top: 58px; width: 100%; text-align: center;
    font-size: 23px; font-weight: 700; color: var(--white);
  }
  .contact-band {
    position: absolute; top: 136px; left: 0; width: 100%; height: 32px;
    background: linear-gradient(90deg, #9a9da5 0%, #eef0f2 30%, #d6d8dc 60%, #f1f2f4 80%, #9c9fa7 100%);
    color: var(--ink-dark); font-size: 16px;
  }
  .contact-item { position: absolute; top: 6px; display: flex; align-items: center; gap: 10px; }
  .contact-item.phone { left: 73px; }
  .contact-item.email { left: 258px; }
  .services {
    position: absolute; top: 178px; width: 100%; text-align: center;
    font-size: 14px; color: var(--text-soft);
  }
  .payments {
    position: absolute; top: 256px; left: 0; width: 100%;
    display: flex; justify-content: center; gap: 10px;
  }
  .payment-chip {
    width: 36px; height: 18px; border-radius: 3px;
    background: var(--chip);
  }
</style>
</head>
<body>
  <main class="card-set">
    <section class="card card-front" aria-label="Card front">
      <div class="brand-mark">LARKMOOR</div>
      <h1 class="company-name silver-text">LARKMOOR CORPORATE CARS</h1>
      <p class="company-web">www.lkcx.com.au</p>
    </section>

    <section class="card card-back" aria-label="Card back">
      <h2 class="person-name">Dean Kovalik</h2>
      <div class="contact-band">
        <div class="contact-item phone">
          <svg width="12" height="20" viewBox="0 0 12 20" aria-hidden="true">
            <rect x="0.5" y="0.5" width="11" height="19" rx="1.5" fill="#222"/>
            <rect x="2" y="2.5" width="8" height="6" fill="#ddd"/>
            <g fill="#ddd"><rect x="2" y="10.5" width="2" height="1.6"/><rect x="5" y="10.5" width="2" height="1.6"/><rect x="8" y="10.5" width="2" height="1.6"/><rect x="2" y="13.5" width="2" height="1.6"/><rect x="5" y="13.5" width="2" height="1.6"/><rect x="8" y="13.5" width="2" height="1.6"/><rect x="2" y="16.5" width="2" height="1.6"/><rect x="5" y="16.5" width="2" height="1.6"/><rect x="8" y="16.5" width="2" height="1.6"/></g>
          </svg>
          <span>0400193726</span>
        </div>
        <div class="contact-item email">
          <svg width="22" height="15" viewBox="0 0 22 15" aria-hidden="true">
            <rect x="0" y="0" width="22" height="15" fill="#111"/>
            <polyline points="1,1 11,9 21,1" fill="none" stroke="#eee" stroke-width="1.5"/>
          </svg>
          <span>bookings@lkcx.com.au</span>
        </div>
      </div>
      <p class="services">airport transfers • corporate travel • special occasions • tours</p>
      <div class="payments" role="img" aria-label="Accepted payment methods">
        <span class="payment-chip"></span>
        <span class="payment-chip"></span>
        <span class="payment-chip"></span>
        <span class="payment-chip"></span>
        <span class="payment-chip"></span>
      </div>
    </section>
  </main>
</body>
</html>
```